Redesign Of Facebook Page Banner and Profile image

I just want to redesign my facebook page to be not so busy....more clean professional dental look. I dont like stock images so much so please go down the newsfeed to use an image or two from it...so it looks personable.

https://www.pagorvex.com/RowanOakDental/

Target Market(s)

Consumers that care about their looks

Industry/Entity Type

Dental Clinic

Requirements
Must have
• I just want to redesign my facebook page to be not so busy....more clean professional modern look. I don't like stock images so much so please go down the newsfeed to use an image or two from it...so it looks personable.
• https://www.pagorvex.com/RowanOakDental/
Nice to have
• I just want to redesign my facebook page to be not so busy....more clean professional dental look. I dont like stock images so much so please go down the newsfeed to use an image or two from it...so it looks personable.
Should not have

```html
<!DOCTYPE html>
<html lang="en">
<head>
<meta charset="utf-8">
<title>Rowan Oak Dental – Cover Banner</title>
<link rel="stylesheet" href="https://fonts.googleapis.com/css2?family=Arimo:wght@400;700&display=swap">
<style>
  :root {
    --backdrop: #333333;
    --sky-deep: #1d83d4;
    --sky-mid: #5aa9e2;
    --sky-pale: #eaf3fb;
    --ribbon: #f4e333;
    --ink: #363636;
    --paper: #ffffff;
    --brand-teal: #2a9fc9;
    --pin-red: #e0202a;
    --photo-warm: #b9aa97;
    --photo-cool: #9fb0c2;
  }
  * { margin: 0; padding: 0; box-sizing: border-box; }
  html, body { width: 1200px; height: 701px; overflow: hidden; background: var(--backdrop); }
  body { font-family: "Arimo", Arial, sans-serif; }

  .canvas { position: relative; width: 1200px; height: 701px; }

  .cover {
    position: absolute; left: 31px; top: 111px; width: 1132px; height: 420px;
    overflow: hidden;
    background: linear-gradient(160deg, var(--sky-deep) 0%, var(--sky-mid) 42%, var(--sky-pale) 88%);
  }

  .offer-ribbon { position: absolute; left: 0; top: 0; width: 360px; height: 260px; }

  .badge-circle {
    position: absolute; left: 192px; top: 89px; width: 90px; height: 90px; border-radius: 50%;
    background: radial-gradient(circle at 40% 35%, #ffffff 0%, #d9dde2 60%, #9aa3ad 100%);
  }

  .headline {
    position: absolute; left: 80px; top: 196px;
    font-weight: 700; font-size: 45px; line-height: 46px; color: var(--ink);
    letter-spacing: 0.2px;
  }

  .contact-box {
    position: absolute; left: 81px; top: 296px; width: 474px; height: 90px;
    background: var(--ribbon);
  }
  .contact-phone {
    position: absolute; left: 12px; top: 6px;
    font-weight: 700; font-size: 51px; line-height: 56px; color: var(--ink);
  }
  .contact-web {
    position: absolute; left: 15px; top: 64px;
    font-size: 18px; line-height: 20px; color: var(--ink);
  }

  .snapshot {
    position: absolute; background: var(--paper);
    box-shadow: 8px 8px 0 rgba(0,0,0,0.18);
  }
  .snapshot--first { left: 601px; top: 26px; width: 245px; height: 285px; transform: rotate(-3deg); }
  .snapshot--second { left: 857px; top: 88px; width: 268px; height: 318px; transform: rotate(4deg); }

  .snapshot-photo { position: absolute; }
  .snapshot--first .snapshot-photo {
    left: 18px; top: 19px; width: 215px; height: 208px;
    background: linear-gradient(180deg, #e9eef3 0%, var(--photo-cool) 55%, #31506f 100%);
  }
  .snapshot--second .snapshot-photo {
    left: 23px; top: 31px; width: 233px; height: 229px;
    background: linear-gradient(180deg, #e7eaee 0%, var(--photo-warm) 60%, #6f6457 100%);
  }

  .snapshot-caption {
    position: absolute; left: 0; right: 0; display: flex; align-items: center; justify-content: center; gap: 6px;
    font-weight: 700; font-size: 15px; color: var(--brand-teal);
  }
  .snapshot--first .snapshot-caption { top: 240px; }
  .snapshot--second .snapshot-caption { top: 273px; }
  .caption-dot { width: 26px; height: 26px; border-radius: 50%; background: #c9d0d7; }

  .pushpin { position: absolute; width: 28px; height: 44px; }
  .snapshot--first .pushpin { left: 108px; top: -22px; }
  .snapshot--second .pushpin { left: 158px; top: -20px; }
</style>
</head>
<body>
<div class="canvas">
  <section class="cover">
    <svg class="offer-ribbon" viewBox="0 0 360 260" aria-label="$99 limited time special">
      <polygon points="0,178 0,215 323,0 262,0" fill="var(--ribbon)"/>
      <g transform="translate(44,198) rotate(-33.5)">
        <text x="0" y="0" font-family="Arimo, Arial, sans-serif" font-weight="700" font-size="48" fill="#363636">$99</text>
        <text x="104" y="-22" font-family="Arimo, Arial, sans-serif" font-weight="700" font-size="16" fill="#363636">LIMITED TIME</text>
        <text x="104" y="-4" font-family="Arimo, Arial, sans-serif" font-weight="700" font-size="16" fill="#363636">SPECIAL</text>
      </g>
    </svg>

    <div class="badge-circle"></div>

    <h1 class="headline">SCHEDULE AN<br>APPOINTMENT TODAY</h1>

    <div class="contact-box">
      <p class="contact-phone">Call 888.555.0142</p>
      <p class="contact-web">www.rowanOakDental.com</p>
    </div>

    <figure class="snapshot snapshot--first">
      <div class="snapshot-photo" role="img" aria-label="Photo of a smiling patient holding a sign, standing between two clinic staff in navy scrubs"></div>
      <figcaption class="snapshot-caption"><span class="caption-dot"></span>Rowan Oak Dental</figcaption>
      <svg class="pushpin" viewBox="0 0 28 44"><line x1="14" y1="22" x2="14" y2="42" stroke="#9aa3ab" stroke-width="2"/><circle cx="14" cy="14" r="11" fill="var(--pin-red)"/><circle cx="10" cy="10" r="3" fill="#ff8a8f"/></svg>
    </figure>

    <figure class="snapshot snapshot--second">
      <div class="snapshot-photo" role="img" aria-label="Photo of a happy patient holding a sign, standing between two clinic staff in tan scrubs"></div>
      <figcaption class="snapshot-caption"><span class="caption-dot"></span>Rowan Oak Dental</figcaption>
      <svg class="pushpin" viewBox="0 0 28 44"><line x1="14" y1="22" x2="14" y2="42" stroke="#9aa3ab" stroke-width="2"/><circle cx="14" cy="14" r="11" fill="var(--pin-red)"/><circle cx="10" cy="10" r="3" fill="#ff8a8f"/></svg>
    </figure>
  </section>
</div>
</body>
</html>
```